design an extra page for our profile

we are looking for someone to create another page like the attached but with the below changes:
heading changed to (Construction)
icons changed and names to reflect new services i.e
- Residential Building
- Commercial Building
- Landscaping
- Concrete
- Painting

the very bottom of the page is to stay the same with our office info

```html
<!DOCTYPE html>
<html lang="en">
<head>
<meta charset="utf-8">
<title>Construction – Services Page</title>
<link rel="stylesheet" href="https://fonts.googleapis.com/css2?family=Montserrat:wght@400;700;800;900&family=Source+Sans+3:wght@400;500&display=swap">
<style>
  :root {
    --navy: #2e3f8f;
    --ink: #0d0d14;
    --white: #ffffff;
    --mist-1: #c9dcea;
    --mist-2: #e6eef8;
    --mist-3: #f2f6fc;
    --photo-1: #b9c7dc;
    --photo-2: #e9eef6;
    --photo-3: #9fb0c8;
  }
  * { margin: 0; padding: 0; box-sizing: border-box; }
  html, body { width: 927px; height: 1200px; overflow: hidden; background: var(--white); }
  .page {
    position: relative;
    width: 927px;
    height: 1200px;
    overflow: hidden;
    background:
      radial-gradient(ellipse 160px 220px at 40px 320px, rgba(170,210,210,.55), transparent 70%),
      radial-gradient(ellipse 300px 160px at 460px 280px, rgba(170,200,225,.6), transparent 70%),
      linear-gradient(180deg, var(--mist-1) 0%, var(--mist-2) 45%, var(--mist-3) 100%);
  }
  .masthead {
    position: absolute; left: 0; top: 0; width: 927px; height: 266px;
    background: var(--navy); color: var(--white); text-align: center;
  }
  .masthead__title {
    font-family: "Montserrat", sans-serif; font-weight: 700;
    font-size: 47px; letter-spacing: 0.5px; line-height: 1;
    padding-top: 36px;
  }
  .masthead__offer {
    font-family: "Source Sans 3", sans-serif; font-weight: 400;
    font-size: 31.5px; line-height: 45px; margin-top: 32px;
  }
  .service {
    position: absolute; width: 260px; margin-left: -130px;
    text-align: center; color: var(--navy);
  }
  .service svg { display: block; margin: 0 auto; fill: var(--navy); }
  .service__name {
    position: absolute; left: 0; width: 260px;
    font-family: "Montserrat", sans-serif; font-weight: 900;
    font-size: 16.5px; letter-spacing: 0.3px; color: var(--ink);
  }
  .service--residential { left: 181px; top: 405px; }
  .service--commercial  { left: 479px; top: 368px; }
  .service--landscaping { left: 764px; top: 370px; }
  .service--concrete    { left: 308px; top: 614px; }
  .service--painting    { left: 632px; top: 610px; }
  .service--residential .service__name { top: 137px; }
  .service--commercial  .service__name { top: 174px; }
  .service--landscaping .service__name { top: 172px; }
  .service--concrete    .service__name { top: 106px; }
  .service--painting    .service__name { top: 110px; }
  .venue-photo {
    position: absolute; left: 65px; top: 762px; width: 794px; height: 340px;
    background:
      linear-gradient(180deg, var(--photo-2) 0%, var(--photo-1) 30%, var(--photo-3) 55%, var(--photo-2) 75%, var(--photo-1) 100%);
  }
  .footer {
    position: absolute; left: 0; top: 1109px; width: 927px; height: 91px;
    background: var(--navy); color: var(--white);
  }
  .footer__brand {
    position: absolute; left: 40px; top: 33px;
    display: flex; align-items: center; gap: 7px;
    font-family: "Montserrat", sans-serif; font-weight: 700; font-size: 19px;
  }
  .footer__brand-dot { width: 10px; height: 10px; border-radius: 50%; background: var(--white); }
  .footer__office {
    position: absolute; left: 178px; top: 16px;
    font-family: "Source Sans 3", sans-serif; font-size: 20px; white-space: nowrap;
  }
  .footer__office strong { font-family: "Montserrat", sans-serif; font-weight: 800; font-size: 18.5px; }
  .footer__office .gap { display: inline-block; width: 12px; }
  .footer__rule {
    position: absolute; left: 177px; top: 44px; width: 698px; height: 1.5px; background: var(--white);
  }
  .footer__web {
    position: absolute; left: 179px; top: 54px; white-space: nowrap;
    font-family: "Montserrat", sans-serif; font-weight: 800; font-size: 14.5px;
  }
  .footer__cities {
    position: absolute; left: 470px; top: 53px; white-space: nowrap;
    font-family: "Montserrat", sans-serif; font-weight: 400; font-size: 15.5px; letter-spacing: 0.6px;
  }
</style>
</head>
<body>
<div class="page">
  <header class="masthead">
    <h1 class="masthead__title">CONSTRUCTION</h1>
    <p class="masthead__offer">AS NEW TENANTS TO THE BUILDING AND AS A WAY<br>OF INTRODUCING OURSELVES WE WOULD LIKE TO OFFER<br>A 10% DISCOUNT ON ANY OF THE BELOW SERVICES.</p>
  </header>

  <div class="service service--residential">
    <svg width="182" height="88" viewBox="0 0 182 88" aria-hidden="true">
      <path d="M91 0 L132 30 L132 8 L142 8 L142 38 L150 45 L143 51 L135 45 L135 88 L115 88 L115 57 L100 57 L100 88 L53 88 L53 45 L44 51 L38 45 Z"/>
      <path d="M25 45 L45 59 L41 63 L38 60 L38 87 L31 87 L31 72 L21 72 L21 87 L6 87 L6 60 L2 63 L0 59 Z"/>
      <path d="M157 45 L182 59 L178 63 L175 60 L175 86 L166 86 L166 71 L156 71 L156 86 L145 86 L145 60 L141 63 L139 59 Z"/>
    </svg>
    <div class="service__name">RESIDENTIAL BUILDING</div>
  </div>

  <div class="service service--commercial">
    <svg width="134" height="138" viewBox="0 0 134 138" aria-hidden="true">
      <g>
        <rect x="70" y="0" width="12" height="6"/>
        <rect x="66" y="6" width="34" height="92"/>
        <rect x="33" y="18" width="12" height="4"/>
        <rect x="33" y="20" width="34" height="82"/>
        <rect x="0" y="102" width="134" height="36"/>
        <rect x="36" y="94" width="64" height="10"/>
        <rect x="104" y="84" width="30" height="20"/>
        <rect x="22" y="104" width="16" height="6"/>
      </g>
      <g fill="#dbe6f3">
        <rect x="72" y="14" width="5" height="5"/><rect x="80" y="14" width="5" height="5"/><rect x="88" y="14" width="5" height="5"/>
        <rect x="72" y="24" width="5" height="5"/><rect x="80" y="24" width="5" height="5"/><rect x="88" y="24" width="5" height="5"/>
        <rect x="80" y="40" width="5" height="16"/>
        <rect x="72" y="66" width="5" height="5"/><rect x="80" y="66" width="5" height="5"/><rect x="88" y="66" width="5" height="5"/>
        <rect x="72" y="78" width="5" height="5"/><rect x="80" y="78" width="5" height="5"/><rect x="88" y="78" width="5" height="5"/>
        <rect x="40" y="30" width="4" height="4"/><rect x="47" y="30" width="4" height="4"/><rect x="54" y="30" width="4" height="4"/>
        <rect x="40" y="38" width="4" height="4"/><rect x="47" y="38" width="4" height="4"/><rect x="54" y="38" width="4" height="4"/>
        <rect x="40" y="56" width="4" height="4"/><rect x="47" y="56" width="4" height="4"/><rect x="54" y="56" width="4" height="4"/>
        <rect x="40" y="64" width="4" height="4"/><rect x="47" y="64" width="4" height="4"/><rect x="54" y="64" width="4" height="4"/>
        <rect x="40" y="84" width="20" height="3"/>
        <rect x="6" y="114" width="4" height="4"/><rect x="13" y="114" width="4" height="4"/><rect x="20" y="114" width="4" height="4"/>
        <rect x="6" y="122" width="4" height="4"/><rect x="13" y="122" width="4" height="4"/><rect x="20" y="122" width="4" height="4"/>
        <rect x="38" y="106" width="5" height="5"/><rect x="46" y="106" width="5" height="5"/><rect x="54" y="106" width="5" height="5"/>
        <rect x="38" y="116" width="5" height="5"/><rect x="46" y="116" width="5" height="5"/><rect x="54" y="116" width="5" height="5"/>
        <rect x="70" y="108" width="20" height="4"/>
        <rect x="72" y="120" width="4" height="4"/><rect x="79" y="120" width="4" height="4"/><rect x="86" y="120" width="4" height="4"/>
        <rect x="106" y="92" width="5" height="5"/><rect x="114" y="92" width="5" height="5"/><rect x="122" y="92" width="5" height="5"/>
        <rect x="106" y="104" width="5" height="5"/><rect x="114" y="104" width="5" height="5"/><rect x="122" y="104" width="5" height="5"/>
        <rect x="106" y="116" width="5" height="5"/><rect x="114" y="116" width="5" height="5"/><rect x="122" y="116" width="5" height="5"/>
        <rect x="62" y="126" width="6" height="12"/><rect x="108" y="128" width="8" height="10"/>
      </g>
    </svg>
    <div class="service__name">COMMERCIAL BUILDING</div>
  </div>

  <div class="service service--landscaping">
    <svg width="116" height="136" viewBox="0 0 116 136" aria-hidden="true">
      <path d="M112 0 C70 4 48 30 54 66 C62 40 80 22 96 12 C82 26 66 48 60 80 L64 82 C70 60 100 40 112 0 Z"/>
      <path d="M4 36 C30 30 50 44 50 70 C40 60 30 52 16 46 C30 56 40 66 46 74 C26 74 10 58 4 36 Z"/>
      <path d="M58 80 L64 86 L18 132 L12 126 Z"/>
      <path d="M8 110 L28 134 L24 136 L4 112 Z"/>
      <path d="M6 118 L0 122 M10 122 L4 126 M14 126 L8 130 M18 130 L12 134" stroke="#2e3f8f" stroke-width="2.5"/>
      <path d="M48 80 L52 76 L86 112 L82 116 Z"/>
      <path d="M80 110 C88 100 102 104 106 116 C108 126 102 134 92 132 Z"/>
    </svg>
    <div class="service__name">LANDSCAPING</div>
  </div>

  <div class="service service--concrete">
    <svg width="102" height="90" viewBox="0 0 102 90" aria-hidden="true">
      <path d="M2 4 L10 0 L14 8 L10 10 L24 34 L20 36 Z M4 4 L12 2" />
      <path d="M18 34 C26 28 36 32 42 44 L40 54 C30 52 20 46 18 34 Z"/>
      <path d="M0 90 L6 82 L10 70 L24 66 L34 56 L46 56 L54 50 L62 56 L70 62 L78 80 L80 90 Z"/>
      <circle cx="68" cy="52" r="3"/><circle cx="78" cy="50" r="4"/><circle cx="68" cy="44" r="2.5"/>
      <circle cx="86" cy="58" r="2.5"/><circle cx="90" cy="72" r="6"/><circle cx="84" cy="84" r="2"/>
      <circle cx="96" cy="86" r="2.5"/><circle cx="98" cy="62" r="2"/>
    </svg>
    <div class="service__name">CONCRETE</div>
  </div>

  <div class="service service--painting">
    <svg width="82" height="92" viewBox="0 0 82 92" aria-hidden="true">
      <rect x="0" y="0" width="74" height="24" rx="6"/>
      <path d="M74 10 L80 12 L80 30 L44 38 L44 46" fill="none" stroke="#2e3f8f" stroke-width="3"/>
      <rect x="38" y="44" width="12" height="48" rx="3"/>
      <path d="M0 36 L34 36 L34 54 L0 54 Z M2 36 L4 38 L6 36 L8 38 L10 36"/>
      <rect x="0" y="56" width="34" height="7"/>
      <path d="M10 63 L24 63 L20 92 L14 92 Z"/>
    </svg>
    <div class="service__name">PAINTING</div>
  </div>

  <div class="venue-photo" role="img" aria-label="Photo of a bright, spacious shopping centre concourse with polished floors and a glass balustrade"></div>

  <footer class="footer">
    <div class="footer__brand"><span class="footer__brand-dot"></span>KESTREL</div>
    <div class="footer__office"><strong>HOME OFFICE:</strong> 1300 00 4821.<span class="gap"></span>Suite 2.04, 18 Harbourline Avenue Northmead</div>
    <div class="footer__rule"></div>
    <div class="footer__web">WWW.KESTREL-SERVICES.COM.AU</div>
    <div class="footer__cities">SYDNEY | CANBERRA | BRISBANE | MELBOURNE</div>
  </footer>
</div>
</body>
</html>
```